Simple+Professional tech feel + warm and friendly box design for pet test kit

Project Name: 10-Minute Canine & Feline Rapid Test Kit Packaging Design
Target Brand Reference: VETRALUX (South Korea) styles
Design Style Direction: Professional tech feel + warm and friendly
Professionalism (Professional): Clear typography and distinct information hierarchy to reflect the product’s scientific rigor and accuracy.
Technological: Reflected through clean graphics and a minimalist layout.
Friendly: Utilise soft, warm colour combinations to convey care for pets and well-wishes for their health.
International: The design should align with mainstream aesthetics and avoid cultural ambiguities.

Target Market(s)
European Union and the United States
Industry/Entity Type
Veterinary Medical
Look and feel
Each slider illustrates characteristics of the customer's brand and the style your logo design should communicate.

```html
<!DOCTYPE html>
<html lang="en">
<head>
<meta charset="utf-8">
<title>ClaroVet – 10-Minute Canine &amp; Feline Rapid Test Kit Packaging</title>
<link rel="stylesheet" href="https://fonts.googleapis.com/css2?family=Encode+Sans+Semi+Condensed:wght@400;500;600;700&family=Lato:wght@400;700&display=swap">
<style>
  :root{
    --magenta:#d4176f;
    --magenta-deep:#c0136a;
    --green:#6cbd45;
    --white:#ffffff;
    --panel-grey:#f3f3f4;
    --stage:#e9e9ec;
    --ink:#d4176f;
    --orange:#e8762d;
    --grey-text:#8a8a8f;
  }
  *{box-sizing:border-box;margin:0;padding:0}
  html,body{width:718px;height:1200px;overflow:hidden}
  body{background:var(--stage);font-family:"Lato",sans-serif;position:relative}
  .panel{position:absolute;overflow:hidden;box-shadow:0 2px 10px rgba(0,0,0,.08)}
  .brand-name{font-family:"Encode Sans Semi Condensed",sans-serif;font-weight:700;color:var(--magenta);letter-spacing:-.5px;line-height:1}
  .tm{font-size:.3em;vertical-align:top;margin-left:2px}

  /* Front panel */
  .front{left:29px;top:40px;width:660px;height:300px;background:var(--white)}
  .front .brand-name{position:absolute;left:36px;top:46px;font-size:56px}
  .front .tests-tag{position:absolute;right:28px;top:90px;background:var(--green);color:var(--white);
    font-family:"Encode Sans Semi Condensed",sans-serif;font-weight:500;font-size:16px;padding:4px 12px 4px 22px;
    clip-path:polygon(10px 0,100% 0,100% 100%,0 100%)}
  .front .title-band{position:absolute;left:0;right:28px;top:120px;height:46px;background:var(--magenta);color:var(--white);
    font-family:"Encode Sans Semi Condensed",sans-serif;font-weight:500;font-size:28px;line-height:46px;padding-left:36px}
  .front .audience-band{position:absolute;left:0;top:166px;width:330px;height:30px;background:var(--green);color:var(--white);
    font-family:"Encode Sans Semi Condensed",sans-serif;font-size:16px;letter-spacing:.5px;line-height:30px;padding-left:36px;
    clip-path:polygon(0 0,100% 0,calc(100% - 14px) 100%,0 100%)}
  .front .pet-art{position:absolute;right:40px;top:176px;width:120px;height:100px;border-radius:10px;
    background:linear-gradient(160deg,#fbe3ef,#f6c4dc)}
  .front .maker{position:absolute;left:36px;bottom:30px;font-family:"Encode Sans Semi Condensed",sans-serif;font-weight:600;font-size:22px;color:var(--magenta)}
  .baseline{position:absolute;left:0;right:0;height:2px;background:var(--green)}
  .front .baseline{bottom:16px}

  /* Top lid */
  .lid{left:29px;top:360px;width:660px;height:120px;background:linear-gradient(90deg,var(--magenta-deep),var(--magenta));
    display:flex;flex-direction:column;align-items:center;justify-content:center;gap:6px}
  .lid .brand-name{color:var(--white);font-size:46px}
  .lid .lid-sub{color:var(--white);font-size:11px;border-top:1px solid rgba(255,255,255,.7);padding-top:4px;letter-spacing:.3px}

  /* Back panel */
  .back{left:29px;top:500px;width:660px;height:300px;background:var(--panel-grey)}
  .back .brand-name{position:absolute;left:36px;top:30px;font-size:48px}
  .back .tests{position:absolute;right:40px;top:40px;font-family:"Encode Sans Semi Condensed",sans-serif;font-size:18px;color:var(--magenta)}
  .back .lot-info{position:absolute;left:36px;top:100px;font-size:9px;color:var(--grey-text);line-height:16px}
  .back .rule{position:absolute;left:36px;top:188px;width:380px;height:1px;background:#b9b9bd}
  .back .vet-only{position:absolute;left:36px;top:170px;font-size:10px;color:var(--orange)}
  .back .maker{position:absolute;left:36px;bottom:30px;font-family:"Encode Sans Semi Condensed",sans-serif;font-weight:600;font-size:20px;color:var(--magenta)}
  .back .pet-art{position:absolute;right:40px;bottom:30px;width:60px;height:80px;border-radius:8px;background:linear-gradient(160deg,#fbe3ef,#f6c4dc)}
  .back .baseline{bottom:16px}

  /* End panel */
  .end{left:179px;top:820px;width:360px;height:340px;background:var(--white)}
  .end .brand-name{position:absolute;left:20px;top:22px;font-size:30px}
  .end .tagline{position:absolute;left:20px;top:64px;font-family:"Encode Sans Semi Condensed",sans-serif;font-size:19px;color:var(--magenta);line-height:1.2}
  .end .tagline em{font-style:normal}
  .end .tagline strong{font-weight:600}
  .end .company{position:absolute;left:20px;right:0;top:126px;background:var(--magenta);color:var(--white);padding:8px 12px 8px 12px}
  .end .company h2{font-family:"Encode Sans Semi Condensed",sans-serif;font-size:17px;font-weight:600;margin-bottom:4px}
  .end .company p{font-size:12px;display:flex;align-items:center;gap:6px;line-height:18px}
  .end .company svg{width:11px;height:11px;fill:none;stroke:var(--white);stroke-width:1.6}
  .end .read-note{position:absolute;left:20px;right:0;top:206px;background:var(--green);color:var(--white);font-size:10px;line-height:13px;padding:4px 12px}
  .end .symbols{position:absolute;left:20px;top:246px;display:flex;align-items:center;gap:12px;color:var(--magenta)}
  .end .symbols svg{width:26px;height:26px;fill:none;stroke:var(--magenta);stroke-width:1.8}
  .end .ivd{border:1.5px solid var(--magenta);font-size:12px;padding:2px 6px}
  .end .temp{font-size:11px}
  .end .storage{position:absolute;left:20px;top:282px;font-family:"Encode Sans Semi Condensed",sans-serif;font-size:12px;color:var(--magenta);line-height:15px}
  .end .baseline{bottom:14px}
</style>
</head>
<body>

<section class="panel front">
  <div class="brand-name">ClaroVet<span class="tm">TM</span></div>
  <div class="tests-tag">5 Tests/Kit</div>
  <div class="title-band">10-Minute Canine &amp; Feline Rapid Test Kit</div>
  <div class="audience-band">FOR DOGS AND CATS</div>
  <div class="pet-art" role="img" aria-label="Line illustration of a dog and a cat sitting side by side"></div>
  <div class="maker">Mirelan</div>
  <div class="baseline"></div>
</section>

<section class="panel lid">
  <div class="brand-name">ClaroVet<span class="tm">TM</span></div>
  <div class="lid-sub">10-Minute Canine &amp; Feline Rapid Test Kit</div>
</section>

<section class="panel back">
  <div class="brand-name">ClaroVet<span class="tm">TM</span></div>
  <div class="tests">5 Tests/Kit</div>
  <div class="lot-info">
    <p>Lot / Lot</p>
    <p>Exp. / Exp.</p>
    <p>Cat. No.: RC-2050</p>
    <p>REF: RCA 0050</p>
  </div>
  <div class="vet-only">Veterinary use only / Usage vétérinaire seulement</div>
  <div class="rule"></div>
  <div class="maker">Mirelan</div>
  <div class="pet-art" role="img" aria-label="Small line illustration of a dog and a cat"></div>
  <div class="baseline"></div>
</section>

<section class="panel end">
  <div class="brand-name">ClaroVet<span class="tm">TM</span></div>
  <div class="tagline"><em>A Clear View into Pet Health</em><br><strong>Made by Mirelan</strong></div>
  <div class="company">
    <h2>Mirelan Biotech Limited</h2>
    <p><svg viewBox="0 0 12 12"><circle cx="6" cy="6" r="5"/><path d="M1 6h10M6 1c2 2 2 8 0 10M6 1c-2 2-2 8 0 10"/></svg>www.mirelan-bio.example</p>
    <p><svg viewBox="0 0 12 12"><rect x="1" y="2.5" width="10" height="7"/><path d="M1 2.5l5 4 5-4"/></svg>sales@mirelan-bio.example</p>
  </div>
  <div class="read-note">(For accurate results, please read<br>the instructions carefully before use)</div>
  <div class="symbols">
    <svg viewBox="0 0 26 26"><circle cx="13" cy="13" r="11"/><path d="M5 21L21 5"/><path d="M9.5 10a3.5 3.5 0 017 0c0 3-7 5-7 8h7"/></svg>
    <svg viewBox="0 0 26 26"><path d="M3 12a10 8 0 0120 0z"/><path d="M13 12v9a2 2 0 01-4 0"/></svg>
    <svg viewBox="0 0 26 26"><circle cx="13" cy="13" r="5"/><path d="M13 2v4M13 20v4M2 13h4M20 13h4M5 5l3 3M18 18l3 3M5 21l3-3M18 8l3-3"/></svg>
    <span class="ivd">IVD</span>
    <span class="temp">4°C – 30°C</span>
  </div>
  <div class="storage">Storage: 2~30°C, moistureproof, avoid light.<br>Note: Disposable, use within validity period.</div>
  <div class="baseline"></div>
</section>

</body>
</html>
```